International Development Cooperation Consultant needs a business card design

I need a business card design for myself as a way to present and introduce to wide range of organisations: international organisations, NGOs, governments, universities....
I am a consultant working in the field of governance, civil society and public sector. I carry out studies and provide advice for development agencies as well as think tanks on different topics such as civil society organisations in developing countries, corruption, climate change, monitoring and evaluation. I also provide technical assistance to governments in developing countries... These studies should help for example NGOs to play a better role in poor countries or where they are threatened, or improved the impact of aid in developing countries. Technical capacity should strengthen the organisation and empower the public civl servants in those countries. I would like to see designs that give a fresh, young, positive, alternative but at the same time serious impression. That reflects change, connecting people, the world, knowledge, multi-culturality... Most of people I have worked with say that 'I make things happen' !
Industry/Entity Type
Business
Contact Information for Business Card
Laia Corbera Vidal
International Development Consultant
Governance Expert
E-mail: laiacorbera@mailnest-example.com
Phone: +34655203817

```html
<!DOCTYPE html>
<html lang="en">
<head>
<meta charset="utf-8">
<title>Laia Corbera Vidal – Business Card</title>
<link rel="stylesheet" href="https://fonts.googleapis.com/css2?family=Michroma&display=swap">
<style>
  :root {
    --backdrop: #b6b7b5;
    --front-centre: #ec5f8d;
    --front-edge: #c0356a;
    --back-teal: #8fd1c9;
    --back-sand: #d3c3a2;
    --back-rose: #e47c90;
    --ink-white: #ffffff;
    --card-shadow: rgba(0, 0, 0, 0.22);
  }
  * { margin: 0; padding: 0; box-sizing: border-box; }
  html, body {
    width: 1200px;
    height: 725px;
    overflow: hidden;
    background: var(--backdrop);
    font-family: "Michroma", "Arial", sans-serif;
    color: var(--ink-white);
  }
  .card-sheet {
    position: relative;
    width: 1200px;
    height: 725px;
    display: flex;
    align-items: center;
    justify-content: center;
    gap: 60px;
  }
  .card {
    position: relative;
    width: 520px;
    height: 297px;
    border-radius: 20px;
    box-shadow: 0 6px 18px var(--card-shadow);
    overflow: hidden;
  }
  .card-front {
    background: radial-gradient(ellipse at 55% 40%, var(--front-centre) 0%, var(--front-edge) 75%);
    display: flex;
    align-items: center;
    padding-left: 64px;
    gap: 22px;
  }
  .mark-square {
    width: 46px;
    height: 46px;
    background: var(--ink-white);
    flex: none;
  }
  .front-name {
    font-size: 22px;
    letter-spacing: 3px;
    font-variant: small-caps;
    white-space: nowrap;
  }
  .card-back {
    background: linear-gradient(165deg, var(--back-teal) 0%, var(--back-teal) 20%, var(--back-sand) 60%, var(--back-rose) 100%);
  }
  .back-mark {
    position: absolute;
    left: 78px;
    top: 142px;
    width: 58px;
    height: 58px;
    background: var(--ink-white);
  }
  .back-divider {
    position: absolute;
    left: 196px;
    top: 88px;
    width: 1.5px;
    height: 150px;
    background: var(--ink-white);
  }
  .back-details {
    position: absolute;
    left: 216px;
    top: 94px;
    font-variant: small-caps;
    letter-spacing: 1.2px;
  }
  .back-name {
    font-size: 17px;
    letter-spacing: 2px;
    margin-bottom: 6px;
  }
  .back-role {
    font-size: 9.5px;
    line-height: 1.55;
  }
  .contact-line {
    display: flex;
    align-items: center;
    gap: 8px;
    font-size: 10.5px;
    margin-top: 6px;
  }
  .contact-line svg { flex: none; }
</style>
</head>
<body>
  <main class="card-sheet">
    <section class="card card-front" aria-label="Card front">
      <span class="mark-square" aria-hidden="true"></span>
      <h1 class="front-name">Laia Corbera Vidal</h1>
    </section>

    <section class="card card-back" aria-label="Card back">
      <span class="back-mark" aria-hidden="true"></span>
      <span class="back-divider" aria-hidden="true"></span>
      <div class="back-details">
        <h2 class="back-name">Laia Corbera Vidal</h2>
        <p class="back-role">International Development<br>Consultant Governance Expert</p>
        <p class="contact-line">
          <svg width="12" height="9" viewBox="0 0 12 9" aria-hidden="true">
            <rect x="0.5" y="0.5" width="11" height="8" fill="#fff"/>
            <path d="M0.5 0.5 L6 5 L11.5 0.5" fill="none" stroke="#c9a9a0" stroke-width="1"/>
          </svg>
          laiacorbera@mailnest-example.com
        </p>
        <p class="contact-line">
          <svg width="12" height="11" viewBox="0 0 12 11" aria-hidden="true">
            <path d="M1 4 Q6 0 11 4 L9.5 5.5 L8 4.5 L4 4.5 L2.5 5.5 Z" fill="#fff"/>
            <rect x="2.5" y="6" width="7" height="4.5" rx="1" fill="#fff"/>
          </svg>
          +34655203817
        </p>
      </div>
    </section>
  </main>
</body>
</html>
```